IT’S NOT A CLEANING, IT’S YOUR LIFE! TOP TEN REASONS WHY THIS IS NOT JUST A “CLEANING”

We made a list for our patients to let them know why our hygiene appointments are different than other cleanings. Since this is a lot of information, we would like it easily readable within 4-5 feet but we do not want the post to be HUGE. Please see below:

IT’S NOT A CLEANING, IT’S YOUR LIFE!
TOP TEN REASONS WHY THIS IS NOT JUST A “CLEANING”

10. We make you look better. Healthy teeth and gums are more attractive. Recent studies
show that the smile is the first thing people notice and that people with better looking teeth
are more confident and successful.

9. We can relieve your headaches. During your hygiene visit we evaluate for serious bite
issues, many of which lead to muscle soreness, headaches, and migraines.

8. We check for oral cancer. Oral cancer kills 1 person per hour 24 hours a day. The death rate for oral cancer is higher than cancers we routinely hear about such as cervical, thyroid and skin cancer.

7. We make you smell better. During your hygiene visit we eliminate many of the germs that live under your gum tissue and cause bad breath.

6. We save you money. By utilizing the latest dental technology (digital x-rays, mouth
cameras, and magnification glasses) we can help with early detection of tooth and gum
problems and save you the cost of gum surgery, root canals, and implants.

5. We clean in places you cannot. We clean under the gum line and between teeth where
most of the germs hide and cause dental disease. 40% of the bacteria in your mouth lives in
between your teeth.

4. We prevent pain. We identify tooth decay that can lead to nerve involvement and pain,
root canal, and tooth loss.

3. We save your teeth. Most tooth loss is from periodontal/gum disease. At each visit we
evaluate the health of your gums and bone with our periodontal screening. Periodontal
disease, like high blood pressure, is symptomless until it is in advanced stages.

2. We protect your loved ones. Studies have proven that the bacteria that cause dental
disease can be transmitted from person to person. Think about that the next time you kiss
someone!

1. We prolong life. Researchers have linked the inflammation and infection found in the
mouth to heart attacks, strokes, and Alzheimer’s. By reducing infection in your mouth we can
greatly improve your overall health!

```html
<!DOCTYPE html>
<html lang="en">
<head>
<meta charset="utf-8">
<title>It's Not a Cleaning, It's Your Life</title>
<link rel="stylesheet" href="https://fonts.googleapis.com/css2?family=Titillium+Web:wght@400;600;700&display=swap">
<style>
  :root {
    --ink: #2b2b2b;
    --heading-grey: #636466;
    --brand-blue: #29a9e1;
    --white: #ffffff;
    --skin-warm: #e8cfc3;
    --skin-light: #f4e6df;
  }
  * { margin: 0; padding: 0; box-sizing: border-box; }
  html, body { width: 1200px; height: 900px; overflow: hidden; background: var(--white); }
  .poster {
    position: relative;
    width: 1200px;
    height: 900px;
    background: var(--white);
    font-family: "Titillium Web", Arial, sans-serif;
    color: var(--ink);
    overflow: hidden;
  }
  .smile-photo {
    position: absolute;
    left: 0; top: 0;
    width: 600px; height: 900px;
    background:
      radial-gradient(ellipse 360px 520px at 180px 260px, var(--skin-warm) 0%, var(--skin-light) 55%, rgba(255,255,255,0) 100%),
      linear-gradient(90deg, var(--skin-light) 0%, rgba(255,255,255,0) 95%);
  }
  .headline {
    position: absolute;
    left: 566px; top: 56px;
    display: flex;
    align-items: center;
    color: var(--heading-grey);
    font-weight: 700;
    text-transform: uppercase;
  }
  .headline-lead {
    font-size: 104px;
    line-height: 1;
    letter-spacing: -3px;
    margin-right: 12px;
  }
  .headline-rest {
    font-size: 40px;
    line-height: 38px;
    letter-spacing: 0.3px;
  }
  .reasons-band {
    position: absolute;
    left: 566px; top: 177px;
    width: 634px; height: 72px;
    background: var(--brand-blue);
    color: var(--white);
    padding: 14px 0 0 17px;
    font-size: 18px;
    line-height: 21px;
    text-transform: uppercase;
  }
  .reasons-band strong { font-weight: 700; }
  .reason {
    position: absolute;
    display: flex;
    font-size: 12.6px;
    line-height: 14.8px;
  }
  .reason-number {
    width: 47px;
    flex: none;
    color: var(--brand-blue);
    font-weight: 700;
    font-size: 25px;
    line-height: 22px;
  }
  .reason-text { width: 245px; }
  .col-left { left: 518px; }
  .col-right { left: 857px; }
  .col-right .reason-text { width: 260px; }
</style>
</head>
<body>
<main class="poster">
  <div class="smile-photo" role="img" aria-label="Close-up photograph of a woman's smile with bright healthy teeth"></div>

  <h1 class="headline">
    <span class="headline-lead">It’s</span>
    <span class="headline-rest">Not a cleaning,<br>your life!</span>
  </h1>

  <div class="reasons-band">Top ten reasons why<br>this is not just a “<strong>Cleaning</strong>”</div>

  <section class="reason col-left" style="top:290px">
    <span class="reason-number">10</span>
    <p class="reason-text">We make you look better. Healthy teeth and gums are more attractive. Recent studies show that the smile is the first thing people notice and that people with better looking teeth are more confident and successful</p>
  </section>
  <section class="reason col-right" style="top:290px">
    <span class="reason-number">09</span>
    <p class="reason-text">We can relieve your headaches. During your hygiene visit we evaluate for serious bite issues, many of which lead to muscle soreness, headaches, and migraines</p>
  </section>

  <section class="reason col-left" style="top:400px">
    <span class="reason-number">08</span>
    <p class="reason-text">We check for oral cancer. Oral cancer kills 1 person per hour 24 hours a day. The death rate for oral cancer is higher than cancers we routinely hear about such as cervical, thyroid and skin cancer</p>
  </section>
  <section class="reason col-right" style="top:400px">
    <span class="reason-number">07</span>
    <p class="reason-text">We make you smell better. During your hygiene visit we eliminate many of the germs that live under your gum tissue and cause bad breath.</p>
  </section>

  <section class="reason col-left" style="top:510px">
    <span class="reason-number">06</span>
    <p class="reason-text">We save you money. By utilizing the latest dental technology (digital x-rays, mouth cameras, and magnification glasses) we can help with early detection of tooth and gum problems and save you the cost of gum surgery, root canals, and implants</p>
  </section>
  <section class="reason col-right" style="top:510px">
    <span class="reason-number">05</span>
    <p class="reason-text">We clean in places you cannot. We clean under the gum line and between teeth where most of the germs hide and cause dental disease. 40% of the bacteria in your mouth lives in between your teeth.</p>
  </section>

  <section class="reason col-left" style="top:632px">
    <span class="reason-number">04</span>
    <p class="reason-text">We prevent pain. We identify tooth decay that can lead to nerve involvement and pain, root canal, and tooth loss.</p>
  </section>
  <section class="reason col-right" style="top:632px">
    <span class="reason-number">03</span>
    <p class="reason-text">We save your teeth. Most tooth loss is from periodontal/gum disease. At each visit we evaluate the health of your gums and bone with our periodontal screening. Periodontal disease, like high blood pressure, is symptomless until it is in advanced stages.</p>
  </section>

  <section class="reason col-left" style="top:748px">
    <span class="reason-number">02</span>
    <p class="reason-text">We protect your loved ones. Studies have proven that the bacteria that cause dental disease can be transmitted from person to person. Think about that the next time you kiss someone!</p>
  </section>
  <section class="reason col-right" style="top:748px">
    <span class="reason-number">01</span>
    <p class="reason-text">We prolong life. Researchers have linked the inflammation and infection found in the mouth to heart attacks, strokes, and Alzheimer’s. By reducing infection in your mouth we can greatly improve your overall health!</p>
  </section>
</main>
</body>
</html>
```